Mobile Recording Studio needs business cards

Open to seeing a creative design, but I want to emphasis my logo and minimize the name/title and company information. Possible a fully black background on card.

My company is a mobile sound recording studio. ok to include a my trailer (actual or cartoon) on the card. My initial thought is more straight forward, but a good design will win me over.

SPECS:
CMYK color mode
High (300ppi) raster effect.
cover bleed area
please deliver: Illustrator file with layers and a pdf at completion.

Name and info for the business card:

Mitchell Garvey
ADR Mixer

email: Mitchell@TakebayDub.example

address:
418 - 6057 East Pembury
Vancouver, BC V3R 2T4

phone:
604.419.8827 office

website:
www.TakebayDub.example

FB: @TakebayDub

Instagram: @TheTakebayDub

Industry/Entity Type

Television Production

Contact Information for Business Card

Mitchell Garvey
ADR Mixer

email: Mitchell@TakebayDub.example

address:
418 - 6057 East Pembury
Vancouver, BC V3R 2T4

phone:
604.419.8827 office

website:
www.TakebayDub.example

FB: @TakebayDub

Instagram: @TheTakebayDub

Colors

Designer to choose colors to be used in the design.

Requirements
Must have
• emphasis my logo and minimize the name/title and company information.
• SPECS:
• CMYK color mode
• High (300ppi) raster effect.
• cover bleed area
• please deliver: Illustrator file with layers and a pdf at completion.
Nice to have
• maybe include the following:
• all black background or black theme
• my work trailer (actual or cartoon) refer to Instagram: @TheTakebayDub

```html
<!DOCTYPE html>
<html lang="en">
<head>
<meta charset="utf-8">
<title>Takebay Dub – Business Card</title>
<link rel="stylesheet" href="https://fonts.googleapis.com/css2?family=Cormorant+Garamond:wght@500;600&display=swap">
<style>
  :root {
    --stage: #1c1c1c;
    --card-black: #050505;
    --card-edge: #151515;
    --silver: #cfcfcf;
    --ink-light: #e6e6e6;
    --ink-soft: #b8b8b8;
    --photo-dark: #1a1a1a;
    --photo-mid: #4a4a48;
    --photo-light: #8d8d88;
  }
  * { margin: 0; padding: 0; box-sizing: border-box; }
  html, body {
    width: 1200px; height: 942px; overflow: hidden;
    background: var(--stage);
    font-family: "Cormorant Garamond", Georgia, serif;
  }
  .card {
    position: absolute; left: 250px;
    width: 700px; height: 400px;
    background: radial-gradient(ellipse at 45% 30%, var(--card-edge) 0%, var(--card-black) 70%);
    overflow: hidden;
  }
  .card--front { top: 50px; }
  .card--back { top: 492px; }

  /* Front */
  .brand {
    position: absolute; top: 78px; left: 0; width: 100%;
    text-align: center;
    font-size: 64px; font-weight: 600; letter-spacing: 3px;
    text-transform: uppercase;
    color: var(--silver);
  }
  .person {
    position: absolute; top: 190px; left: 0; width: 100%;
    text-align: center; color: var(--ink-light);
  }
  .person__name { font-size: 28px; font-weight: 600; font-variant: small-caps; letter-spacing: 1px; }
  .person__title { font-size: 16px; font-weight: 600; font-variant: small-caps; letter-spacing: 1.5px; margin-top: 2px; color: var(--ink-soft); }
  .contact {
    position: absolute; left: 44px; right: 44px; bottom: 44px;
    color: var(--ink-light); font-size: 16px; font-weight: 500;
  }
  .contact__row { display: flex; align-items: center; gap: 6px; line-height: 28px; }
  .contact__item { display: inline-flex; align-items: center; gap: 5px; margin-right: 14px; }
  .icon { width: 12px; height: 12px; fill: var(--ink-light); flex: none; }

  /* Back */
  .photo-area {
    position: absolute; inset: 0;
    background:
      linear-gradient(90deg, var(--card-black) 0%, rgba(5,5,5,0.85) 22%, rgba(5,5,5,0.2) 55%, rgba(5,5,5,0.6) 100%),
      radial-gradient(ellipse at 62% 55%, var(--photo-light) 0%, var(--photo-mid) 35%, var(--photo-dark) 75%);
  }
  .social {
    position: absolute; top: 26px; left: 30px;
    color: var(--ink-light); font-size: 15px; font-weight: 500;
  }
  .social__item { display: flex; align-items: center; gap: 7px; line-height: 28px; }
  .social__mark { width: 11px; height: 11px; background: var(--ink-light); border-radius: 2px; }
</style>
</head>
<body>

<section class="card card--front">
  <div class="brand">Takebay Dub</div>

  <div class="person">
    <div class="person__name">Mitchell Garvey</div>
    <div class="person__title">ADR Mixer</div>
  </div>

  <div class="contact">
    <div class="contact__row">
      <span class="contact__item">
        <svg class="icon" viewBox="0 0 12 12"><path d="M2.5 0.5 L4.5 0.5 L5.3 3.2 L3.9 4.3 C4.6 5.8 6 7.3 7.7 8.1 L8.8 6.7 L11.5 7.5 L11.5 9.5 C11.5 10.6 10.6 11.5 9.5 11.5 C4.5 11.3 0.7 7.5 0.5 2.5 C0.5 1.4 1.4 0.5 2.5 0.5 Z"/></svg>
        604.419.8827
      </span>
      <span class="contact__item">
        <svg class="icon" viewBox="0 0 12 12"><path d="M0.5 2 H11.5 V10 H0.5 Z M1.5 3 V3.4 L6 6.6 L10.5 3.4 V3 Z" fill-rule="evenodd"/></svg>
        Mitchell@TakebayDub.example
      </span>
      <span class="contact__item">
        <svg class="icon" viewBox="0 0 12 12"><circle cx="6" cy="6" r="5.5"/><circle cx="6" cy="6" r="4" fill="#050505"/><rect x="5.4" y="2" width="1.2" height="8" rx="0.6"/></svg>
        www.TakebayDub.example
      </span>
    </div>
    <div class="contact__row">
      <span class="contact__item">
        <svg class="icon" viewBox="0 0 12 12"><path d="M6 0.5 C3.8 0.5 2.2 2.1 2.2 4.2 C2.2 7 6 11.5 6 11.5 C6 11.5 9.8 7 9.8 4.2 C9.8 2.1 8.2 0.5 6 0.5 Z M6 2.8 A1.4 1.4 0 1 1 6 5.6 A1.4 1.4 0 1 1 6 2.8 Z" fill-rule="evenodd"/></svg>
        418 - 6057 East Pembury, Vancouver, BC V3R 2T4
      </span>
    </div>
  </div>
</section>

<section class="card card--back">
  <div class="photo-area" role="img" aria-label="Photograph of the mobile recording studio trailer and its truck parked at night"></div>
  <div class="social">
    <div class="social__item"><span class="social__mark"></span>@TakebayDub</div>
    <div class="social__item"><span class="social__mark"></span>@TheTakebayDub</div>
  </div>
</section>

</body>
</html>
```